Brindle Logistics Business Card Design

We are a trucking and warehousing company. We run freight in the US manly from the Pacific NW to TX and back up the the PNW. We also do warehousing where we store, move, and distribute freight. Looking for a clean and modern design of business card. We would like to look rich and elegant. Attached is our logo.

Industry/Entity Type

Trucking Company

Contact Information for Business Card

Looking for a clean and modern design of business card. We would like to look rich and elegant.

Font styles to use
Sans Serif

Colors

Designer to choose colors to be used in the design.

Requirements
Must have
• logo but it should not dominate the card
Should not have
• logo should not dominate the card

```html
<!DOCTYPE html>
<html lang="en">
<head>
<meta charset="utf-8">
<title>Brindle Logistics Business Card</title>
<link href="https://fonts.googleapis.com/css2?family=Open+Sans:wght@300;400;600;700&display=swap" rel="stylesheet">
<style>
  :root {
    --bg: #2a2b2e;
    --card: #ffffff;
    --navy: #0f2b45;
    --brand-blue: #1e7fc6;
    --ink: #3a3a3c;
    --ink-soft: #9a9a9c;
    --icon: #1d4a74;
    --rule: #6b6b6d;
  }
  * { box-sizing: border-box; margin: 0; padding: 0; }
  html, body { width: 1200px; height: 1200px; overflow: hidden; }
  body {
    background: var(--bg);
    font-family: "Open Sans", Arial, sans-serif;
    display: flex;
    flex-direction: column;
    align-items: center;
    justify-content: center;
    gap: 60px;
  }
  .card {
    position: relative;
    width: 840px;
    height: 480px;
    border-radius: 36px;
    overflow: hidden;
    box-shadow: 0 18px 40px rgba(0,0,0,.45);
  }

  /* Front */
  .card--front { background: var(--navy); }
  .card--front svg.face { position: absolute; inset: 0; }
  .brand {
    position: absolute;
    inset: 0;
    display: flex;
    align-items: center;
    justify-content: center;
    gap: 22px;
  }
  .brand__dot {
    width: 62px; height: 62px;
    border-radius: 50%;
    background: var(--brand-blue);
  }
  .brand__name {
    font-weight: 600;
    font-size: 50px;
    letter-spacing: 2px;
    color: var(--brand-blue);
    text-transform: uppercase;
  }

  /* Back */
  .card--back { background: var(--card); }
  .fleet-photo {
    position: absolute;
    left: 120px; top: 0;
    width: 720px; height: 300px;
    background: linear-gradient(90deg, rgba(236,236,236,0) 0%, #eeeaea 25%, #f6dcdc 55%, #f3d3d3 85%, #f7eeee 100%);
    opacity: .85;
  }
  .accent-bar {
    position: absolute;
    left: 0; top: 222px;
    width: 14px; height: 70px;
    background: var(--navy);
  }
  .person {
    position: absolute;
    left: 44px; top: 214px;
  }
  .person__name {
    font-weight: 700;
    font-size: 48px;
    line-height: 1;
    color: var(--ink);
    letter-spacing: 1px;
    text-transform: uppercase;
    white-space: nowrap;
  }
  .person__role {
    font-weight: 300;
    font-size: 30px;
    line-height: 1;
    color: var(--ink-soft);
    margin-top: 2px;
    margin-left: 250px;
  }
  .rule {
    position: absolute;
    left: 0; top: 318px;
    width: 440px; height: 2px;
    background: var(--rule);
  }
  .contacts {
    position: absolute;
    list-style: none;
    font-size: 24px;
    color: var(--ink);
    line-height: 1.25;
  }
  .contacts li { display: flex; align-items: flex-start; gap: 12px; margin-bottom: 8px; }
  .contacts svg { flex: 0 0 24px; width: 24px; height: 24px; margin-top: 3px; fill: var(--icon); }
  .contacts--phone { left: 110px; top: 336px; }
  .contacts--web { left: 476px; top: 322px; }
</style>
</head>
<body>

  <section class="card card--front" aria-label="Card front">
    <svg class="face" viewBox="0 0 840 480" aria-hidden="true">
      <path fill="#ffffff" d="M36 0 H804 Q840 0 840 36 V60 Q760 240 840 420 V444 Q840 480 804 480 H36 Q0 480 0 444 V420 Q80 240 0 60 V36 Q0 0 36 0 Z"/>
    </svg>
    <div class="brand">
      <span class="brand__dot"></span>
      <span class="brand__name">Brindle Logistics LLC</span>
    </div>
  </section>

  <section class="card card--back" aria-label="Card back">
    <div class="fleet-photo" role="img" aria-label="Faded photo of a box truck and forklift"></div>
    <div class="accent-bar"></div>
    <div class="person">
      <div class="person__name">Dana Whitfield</div>
      <div class="person__role">President</div>
    </div>
    <div class="rule"></div>

    <ul class="contacts contacts--phone">
      <li>
        <svg viewBox="0 0 24 24" aria-hidden="true"><path d="M6.6 10.8a15.1 15.1 0 0 0 6.6 6.6l2.2-2.2a1 1 0 0 1 1-.25 11.4 11.4 0 0 0 3.6.57 1 1 0 0 1 1 1V20a1 1 0 0 1-1 1A17 17 0 0 1 3 4a1 1 0 0 1 1-1h3.5a1 1 0 0 1 1 1c0 1.25.2 2.45.57 3.570a1 1 0 0 1-.25 1z"/></svg>
        <span>(000) 000-0000,</span>
      </li>
      <li>
        <svg viewBox="0 0 24 24" aria-hidden="true"><path d="M6.6 10.8a15.1 15.1 0 0 0 6.6 6.6l2.2-2.2a1 1 0 0 1 1-.25 11.4 11.4 0 0 0 3.6.57 1 1 0 0 1 1 1V20a1 1 0 0 1-1 1A17 17 0 0 1 3 4a1 1 0 0 1 1-1h3.5a1 1 0 0 1 1 1c0 1.25.2 2.45.57 3.57a1 1 0 0 1-.25 1z"/></svg>
        <span>(000) 000-0000,</span>
      </li>
      <li>
        <svg viewBox="0 0 24 24" aria-hidden="true"><path d="M7 1h10a2 2 0 0 1 2 2v18a2 2 0 0 1-2 2H7a2 2 0 0 1-2-2V3a2 2 0 0 1 2-2zm0 3v15h10V4zm5 16.2a.9.9 0 1 0 0 1.8.9.9 0 0 0 0-1.8z"/></svg>
        <span>(000) 000-0000,</span>
      </li>
    </ul>

    <ul class="contacts contacts--web">
      <li>
        <svg viewBox="0 0 24 24" aria-hidden="true"><path d="M2 5h20v14H2zm2 2v.5l8 5.5 8-5.5V7zm0 2.9V17h16V9.9l-8 5.5z"/></svg>
        <span>info@brindlefreight.com</span>
      </li>
      <li>
        <svg viewBox="0 0 24 24" aria-hidden="true"><path d="M12 2a10 10 0 1 0 0 20 10 10 0 0 0 0-20zm-1 17.9A8 8 0 0 1 4.2 10.6L9 15.4v1a2 2 0 0 0 2 2zm6.9-2.5a2 2 0 0 0-1.9-1.4h-1v-3a1 1 0 0 0-1-1H8v-2h2a1 1 0 0 0 1-1V7h2a2 2 0 0 0 2-2v-.4a8 8 0 0 1 2.9 12.8z"/></svg>
        <span>www.brindlefreight.com</span>
      </li>
      <li>
        <svg viewBox="0 0 24 24" aria-hidden="true"><path d="M12 2a7 7 0 0 0-7 7c0 5.2 7 13 7 13s7-7.8 7-13a7 7 0 0 0-7-7zm0 9.5A2.5 2.5 0 1 1 12 6.5a2.5 2.5 0 0 1 0 5z"/></svg>
        <span>240 Harbor Lane, 3rd<br>Floor, Tacoma, WA 00000</span>
      </li>
    </ul>
  </section>

</body>
</html>
```